Colorful Dog Trainer Business cards

I need a logo that's an illustration of my dog's head - ideally just line work. It will also include my business name (WRENFIELD), Positive Reinforcement Training, my name, my certifications, phone, email, and instagram. Creative card shapes are welcome! I want it to be colorful and eye catching.
Target Market(s)
dog owners in Manhattan and Jersey City
Industry/Entity Type
dog training
Contact Information for Business Card
my business name (WRENFIELD), Positive Reinforcement Training, my name, my certifications, phone, email, and instagram
Look and feel

```html
<!DOCTYPE html>
<html lang="en">
<head>
<meta charset="utf-8">
<title>Wrenfield – Business Card</title>
<link href="https://fonts.googleapis.com/css2?family=Poppins:wght@300;400;500;600;700&display=swap" rel="stylesheet">
<style>
  :root {
    --backdrop: #c8c8c8;
    --brown: #8a5a40;
    --ink: #1c1c1c;
    --paper: #ffffff;
  }
  * { box-sizing: border-box; margin: 0; padding: 0; }
  html, body {
    width: 750px; height: 1200px; overflow: hidden;
    background: var(--backdrop);
    font-family: "Poppins", sans-serif;
  }
  .canvas { position: relative; width: 750px; height: 1200px; }
  .card {
    position: absolute; left: 134px; width: 482px; height: 277px;
    overflow: hidden;
    box-shadow: 6px 8px 10px rgba(0,0,0,.28);
  }
  .card--front { top: 299px; background: var(--paper); }
  .card--back { top: 624px; background: var(--brown); }

  .front-shape { position: absolute; inset: 0; }

  /* business name */
  .business { position: absolute; text-align: center; }
  .business__row { display: flex; align-items: center; justify-content: center; }
  .business__dot { border-radius: 50%; flex: none; }
  .business__name { font-weight: 600; line-height: 1; letter-spacing: 0.5px; }
  .business__tagline { font-weight: 500; letter-spacing: 1.4px; }

  .card--front .business { left: 18px; top: 118px; width: 176px; color: var(--ink); }
  .card--front .business__dot { width: 14px; height: 14px; margin-right: 8px; background: var(--brown); }
  .card--front .business__name { font-size: 20px; }
  .card--front .business__tagline { font-size: 6px; margin-top: 8px; }

  /* contact block */
  .person { position: absolute; left: 265px; top: 26px; color: var(--paper); }
  .person__name { font-size: 25px; font-weight: 300; line-height: 1; }
  .person__name strong { font-weight: 700; }
  .person__role { font-size: 13px; font-weight: 400; line-height: 1.2; }

  .contacts { position: absolute; left: 265px; top: 74px; list-style: none; color: var(--paper); }
  .contact { display: flex; align-items: center; height: 26px; margin-bottom: 5.5px; }
  .contact__icon { width: 26px; height: 26px; flex: none; margin-right: 9px; }
  .contact__text { font-size: 11.2px; line-height: 1.2; }

  .certs { position: absolute; left: 265px; top: 208px; color: var(--paper); }
  .certs__label { font-size: 10px; font-weight: 600; margin-bottom: 2px; }
  .cert {
    display: block; width: 179px; height: 14px; margin-bottom: 4px;
    background: var(--ink); border-radius: 7px;
    font-size: 9.6px; font-weight: 700; line-height: 14px; text-align: center;
  }

  /* back */
  .back-texture {
    position: absolute; right: 0; top: 0; width: 62%; height: 100%;
    background: radial-gradient(ellipse at 75% 35%, rgba(255,255,255,.05), rgba(255,255,255,0) 65%);
  }
  .card--back .business { left: 0; right: 0; top: 96px; color: var(--paper); }
  .card--back .business__dot { width: 22px; height: 22px; margin-right: 12px; background: var(--ink); }
  .card--back .business__name { font-size: 30px; }
  .card--back .business__tagline { font-size: 8px; margin-top: 10px; letter-spacing: 2.4px; }
  .back-web {
    position: absolute; left: 0; right: 0; top: 226px; text-align: center;
    color: var(--paper); font-size: 14px; font-weight: 500; letter-spacing: 2.4px;
  }
</style>
</head>
<body>
<main class="canvas">

  <section class="card card--front" aria-label="Business card front">
    <svg class="front-shape" viewBox="0 0 482 277" aria-hidden="true">
      <path d="M246 0 Q132 138.5 246 277 L482 277 L482 0 Z" fill="var(--brown)"/>
      <path d="M239 0 Q124 138.5 239 277" fill="none" stroke="var(--ink)" stroke-width="3"/>
    </svg>

    <div class="business">
      <div class="business__row">
        <span class="business__dot" aria-hidden="true"></span>
        <span class="business__name">WRENFIELD</span>
      </div>
      <div class="business__tagline">POSITIVE REINFORCEMENT TRAINING</div>
    </div>

    <div class="person">
      <div class="person__name">Mara <strong>Quist</strong></div>
      <div class="person__role">Founder</div>
    </div>

    <ul class="contacts">
      <li class="contact">
        <svg class="contact__icon" viewBox="0 0 26 26" aria-hidden="true">
          <circle cx="13" cy="13" r="12" fill="var(--ink)" stroke="var(--paper)" stroke-width="1.5"/>
          <path d="M9.5 8 L11.3 8 L12 10.6 L10.9 11.5 Q12 14.2 14.5 15.1 L15.4 14 L18 14.7 L18 16.5 Q17.5 17.6 16 17.5 Q9.2 16.6 8.5 10 Q8.5 8.5 9.5 8 Z" fill="var(--paper)"/>
        </svg>
        <span class="contact__text">555 0142 0199</span>
      </li>
      <li class="contact">
        <svg class="contact__icon" viewBox="0 0 26 26" aria-hidden="true">
          <circle cx="13" cy="13" r="12" fill="var(--ink)" stroke="var(--paper)" stroke-width="1.5"/>
          <path d="M13 19 Q8.5 13.5 8.5 11 A4.5 4.5 0 0 1 17.5 11 Q17.5 13.5 13 19 Z" fill="var(--paper)"/>
          <circle cx="13" cy="11" r="1.7" fill="var(--ink)"/>
        </svg>
        <span class="contact__text">48B Harbor Lane 1180<br>elm street</span>
      </li>
      <li class="contact">
        <svg class="contact__icon" viewBox="0 0 26 26" aria-hidden="true">
          <circle cx="13" cy="13" r="12" fill="var(--ink)" stroke="var(--paper)" stroke-width="1.5"/>
          <rect x="8" y="9.5" width="10" height="7" fill="var(--paper)"/>
          <path d="M8 9.5 L13 13.5 L18 9.5" fill="none" stroke="var(--ink)" stroke-width="0.9"/>
        </svg>
        <span class="contact__text">info@wrenfield.com</span>
      </li>
      <li class="contact">
        <svg class="contact__icon" viewBox="0 0 26 26" aria-hidden="true">
          <circle cx="13" cy="13" r="12" fill="var(--ink)" stroke="var(--paper)" stroke-width="1.5"/>
          <g fill="none" stroke="var(--paper)" stroke-width="1">
            <circle cx="13" cy="13" r="5"/>
            <ellipse cx="13" cy="13" rx="2.2" ry="5"/>
            <path d="M8 13 H18 M8.8 10.5 H17.2 M8.8 15.5 H17.2"/>
          </g>
        </svg>
        <span class="contact__text">www.wrenfield.com</span>
      </li>
    </ul>

    <div class="certs">
      <div class="certs__label">Certifications</div>
      <span class="cert">PROFESSIONAL CERTIFICATION</span>
      <span class="cert">PRACTITIONER CERTIFICATION</span>
    </div>
  </section>

  <section class="card card--back" aria-label="Business card back">
    <div class="back-texture" role="img" aria-label="Faint line-art decoration"></div>
    <div class="business">
      <div class="business__row">
        <span class="business__dot" aria-hidden="true"></span>
        <span class="business__name">WRENFIELD</span>
      </div>
      <div class="business__tagline">POSITIVE REINFORCEMENT TRAINING</div>
    </div>
    <div class="back-web">www.wrenfield.com</div>
  </section>

</main>
</body>
</html>
```